Business Card for Marco Thieblin Analytics and Marco Thieblin Photography

I want a double sided business card: on one side it should be about "Marco Thieblin Photography" and on the other side about "Marco Thieblin Analytics". You find the logos for these two projects in the attachments. The design of the business card should blend well with the colours and fonts used in the logos and should be quite simple, yet look professional and modern.

In addition to my name, there should be content for a telephone number, e-mail address and website. There should be little icons (for telephone, email and web) before these fields. I do not want a postal mail address field.
Lastly you should indicate that people can contact me in the following languages: Lëtzebuergesch, Deutsch, Français, English, Castellano, Ido
This should be very unobtrusive: either in a small muted font or with little icons (preferably without using flags as flags represent nations, not languages - one possibility would be by using the 2 letter ISO codes).

The design should be delivered in Adobe Illustrator format or something similar that I can edit easily, as it's possible that I will change my e-mail address and domain soon.

I hope this was detailed enough but still leaves you some freedom for designing something nice.

Thank you!
Marco

Industry/Entity Type

Business

Contact Information for Business Card

e-mail address: mtb_@orvenmail.example
website: www.marcothieblin.example (for Marco Thieblin Photography)
website: kelvodata.example/mtb (for Marco Thieblin Analytics - this address is likely to change)
phone: +352 691 987 654 (not my real number - I prefer not to publish it on the web)

Requirements
Nice to have
• A speech bubble followed by the 2-letter language codes (lb, de, fr, en, es, io) or even speech bubble icons for every language would be nice and eliminates the need to put text like 'you can contact me in the following languages'.

```html
<!DOCTYPE html>
<html lang="en">
<head>
<meta charset="utf-8">
<title>Marco Thieblin – Business Cards</title>
<link rel="stylesheet" href="https://fonts.googleapis.com/css2?family=Lato:wght@400;700&display=swap">
<style>
  :root {
    --ink: #0b0b0b;
    --paper: #ffffff;
    --accent: #f28a1e;
    --backdrop: #2a2a2a;
    --text-dark: #1a1a1a;
    --text-light: #f2f2f2;
  }
  * { box-sizing: border-box; margin: 0; padding: 0; }
  html, body { width: 1200px; height: 880px; overflow: hidden; }
  body {
    background: var(--backdrop);
    font-family: "Lato", Arial, sans-serif;
    position: relative;
  }
  .card {
    position: absolute;
    width: 620px;
    height: 354px;
    left: 290px;
    border-radius: 22px;
    overflow: hidden;
    box-shadow: 0 14px 30px rgba(0,0,0,.45);
  }
  .card--analytics { top: 66px; }
  .card--photography { top: 460px; }
  .card-bg { position: absolute; inset: 0; width: 100%; height: 100%; }

  .contact {
    position: absolute;
    left: 40px;
    top: 60px;
    width: 260px;
    font-size: 15px;
    line-height: 1.3;
  }
  .card--analytics .contact { color: var(--text-light); }
  .card--photography .contact { color: var(--text-dark); }

  .contact-list { list-style: none; margin-bottom: 16px; }
  .contact-item { display: flex; align-items: center; gap: 9px; margin-bottom: 4px; white-space: nowrap; }
  .contact-icon {
    width: 20px; height: 20px; flex: none;
    border: 1.5px solid var(--accent);
    border-radius: 50%;
    display: flex; align-items: center; justify-content: center;
  }
  .contact-icon svg { width: 11px; height: 11px; fill: none; stroke: var(--accent); stroke-width: 1.6; }

  .languages-title {
    font-weight: 700;
    font-size: 14px;
    text-transform: uppercase;
    line-height: 1.2;
    margin-bottom: 8px;
  }
  .language-list { list-style: none; font-size: 16px; line-height: 1.1; }
  .language-code {
    display: inline-block;
    width: 24px;
    color: var(--accent);
    font-weight: 700;
    font-size: 14px;
  }

  .brand {
    position: absolute;
    top: 0; bottom: 0;
    display: flex;
    align-items: center;
    gap: 12px;
    color: var(--accent);
    font-weight: 400;
    font-size: 28px;
    line-height: 1.15;
  }
  .card--analytics .brand { left: 340px; right: 24px; }
  .card--photography .brand { left: 330px; right: 24px; }
  .brand-dot {
    width: 14px; height: 14px; flex: none;
    border-radius: 50%;
    background: var(--accent);
  }
</style>
</head>
<body>

<!-- Analytics side -->
<section class="card card--analytics">
  <svg class="card-bg" viewBox="0 0 620 354" aria-hidden="true">
    <rect width="620" height="354" fill="var(--paper)"/>
    <path d="M0 0 H272 C300 130 370 270 480 354 H0 Z" fill="var(--ink)"/>
    <path d="M272 0 C300 130 370 270 480 354" fill="none" stroke="var(--accent)" stroke-width="4" transform="translate(5 0)"/>
  </svg>

  <div class="contact">
    <ul class="contact-list">
      <li class="contact-item">
        <span class="contact-icon"><svg viewBox="0 0 12 12"><path d="M3 1 L5 3.5 L4 5 C5 7 6 8 7.5 8.5 L9 7.5 L11 9.5 L9.5 11 C5 10.5 1.5 7 1 2.5 Z"/></svg></span>
        +352 691 987 654
      </li>
      <li class="contact-item">
        <span class="contact-icon"><svg viewBox="0 0 12 12"><rect x="1" y="2.5" width="10" height="7"/><path d="M1 2.5 L6 6.5 L11 2.5"/></svg></span>
        mtb_@orvenmail.example
      </li>
      <li class="contact-item">
        <span class="contact-icon"><svg viewBox="0 0 12 12"><circle cx="6" cy="6" r="5"/><path d="M1 6 H11 M6 1 C3.5 4 3.5 8 6 11 M6 1 C8.5 4 8.5 8 6 11"/></svg></span>
        www.marcothieblin.example
      </li>
    </ul>
    <p class="languages-title">Contact me in the<br>following languages</p>
    <ul class="language-list">
      <li><span class="language-code">lb</span>Lëtzebuergesch</li>
      <li><span class="language-code">de</span>Deutsch</li>
      <li><span class="language-code">fr</span>Français</li>
      <li><span class="language-code">en</span>English</li>
      <li><span class="language-code">es</span>Castellano</li>
      <li><span class="language-code">io</span>Ido</li>
    </ul>
  </div>

  <div class="brand">
    <span class="brand-dot"></span>
    <span class="brand-name">Marco Thieblin<br>Analytics</span>
  </div>
</section>

<!-- Photography side -->
<section class="card card--photography">
  <svg class="card-bg" viewBox="0 0 620 354" aria-hidden="true">
    <rect width="620" height="354" fill="var(--ink)"/>
    <path d="M0 0 H296 C310 150 380 280 470 354 H0 Z" fill="var(--paper)"/>
    <path d="M296 0 C310 150 380 280 470 354" fill="none" stroke="var(--accent)" stroke-width="4" transform="translate(5 0)"/>
  </svg>

  <div class="contact">
    <ul class="contact-list">
      <li class="contact-item">
        <span class="contact-icon"><svg viewBox="0 0 12 12"><path d="M3 1 L5 3.5 L4 5 C5 7 6 8 7.5 8.5 L9 7.5 L11 9.5 L9.5 11 C5 10.5 1.5 7 1 2.5 Z"/></svg></span>
        +352 691 987 654
      </li>
      <li class="contact-item">
        <span class="contact-icon"><svg viewBox="0 0 12 12"><rect x="1" y="2.5" width="10" height="7"/><path d="M1 2.5 L6 6.5 L11 2.5"/></svg></span>
        mtb_@orvenmail.example
      </li>
      <li class="contact-item">
        <span class="contact-icon"><svg viewBox="0 0 12 12"><circle cx="6" cy="6" r="5"/><path d="M1 6 H11 M6 1 C3.5 4 3.5 8 6 11 M6 1 C8.5 4 8.5 8 6 11"/></svg></span>
        www.marcothieblin.example
      </li>
    </ul>
    <p class="languages-title">Contact me in the<br>following languages</p>
    <ul class="language-list">
      <li><span class="language-code">lb</span>Lëtzebuergesch</li>
      <li><span class="language-code">de</span>Deutsch</li>
      <li><span class="language-code">fr</span>Français</li>
      <li><span class="language-code">en</span>English</li>
      <li><span class="language-code">es</span>Castellano</li>
      <li><span class="language-code">io</span>Ido</li>
    </ul>
  </div>

  <div class="brand">
    <span class="brand-dot"></span>
    <span class="brand-name">Marco Thieblin<br>Photography</span>
  </div>
</section>

</body>
</html>
```